Letterhead for financial advisor-insurance agent firm

Our company, Marlowe Thistle Insurance & Investments, is an insurance (health, life, home, auto, etc) and investment brokerage offering a suite of options to meet client needs. We need letterhead that is professional and embodies strength, security and sophistication.

Industry/Entity Type

Investment

```html
<!DOCTYPE html>
<html lang="en">
<head>
<meta charset="utf-8">
<title>Marlowe Thistle Insurance &amp; Investments — Letterhead</title>
<link rel="stylesheet" href="https://fonts.googleapis.com/css2?family=Cormorant+Garamond:wght@600&display=swap">
<style>
  :root {
    --navy: #2b3557;
    --rule-grey: #9a9ca3;
    --frame-grey: #6f7075;
    --paper: #ffffff;
  }
  html, body {
    margin: 0;
    padding: 0;
    overflow: hidden;
    background: var(--paper);
  }
  .letterhead {
    position: relative;
    width: 857px;
    height: 1200px;
    background: var(--paper);
    overflow: hidden;
  }
  .page-frame {
    position: absolute;
    left: 7px;
    top: 7px;
    width: 843px;
    height: 1189px;
    border: 1px solid var(--frame-grey);
    box-sizing: border-box;
  }
  .band {
    position: absolute;
    top: 117px;
    height: 16px;
    background: var(--navy);
  }
  .band--left { left: 9px; width: 314px; }
  .band--right { left: 538px; width: 311px; }
  .band-rule {
    position: absolute;
    top: 137px;
    height: 1px;
    background: var(--rule-grey);
  }
  .band-rule--left { left: 9px; width: 314px; }
  .band-rule--right { left: 538px; width: 311px; }
  .company-name {
    position: absolute;
    left: 323px;
    width: 215px;
    top: 109px;
    margin: 0;
    text-align: center;
    color: var(--navy);
    font-family: "Cormorant Garamond", "Times New Roman", serif;
    font-weight: 600;
    font-size: 16px;
    line-height: 18px;
  }
  .company-name span { display: block; }
</style>
</head>
<body>
  <div class="letterhead">
    <div class="page-frame"></div>

    <div class="band band--left"></div>
    <div class="band band--right"></div>
    <div class="band-rule band-rule--left"></div>
    <div class="band-rule band-rule--right"></div>

    <p class="company-name">
      <span>Marlowe Thistle</span>
      <span>Insurance &amp; Investments</span>
    </p>
  </div>
</body>
</html>
```